PINE HOLLOW BUILDERS leave behind sales FLYER 8.5"x11"

We need a high quality advertising flyer 8.5"x11" for our construction company offering kitchen and bathroom remodels. Can be front and back or just the front of the flyer depending on the design. phone number to come
www.brightmortarworks.example

we are also a home inspection company. We will leave this at the home when we are done with our home inspections for our new home owners

Target Market(s)

Home owners

Industry/Entity Type

Residential Construction

Contact Information for Business Card

We want it to match the flyer please

Requirements
Must have
• My logo, my website , my phone number (to come later),
• FL State Lic. #CRC8047163 & Insured
• We Specialize in Bathroom and Kitchen remodeling ,new Construction & Interior or Exterior home Renovations, garages and more! Serving Central Florida for over 15 years.
• Family owned and operated,
• we perform all levels of building and remodeling.
• i wouldn't mind seeing what you come up with for text on the flyer.
Nice to have
• maybe a nice kitchen and bathroom pictures

```html
<!DOCTYPE html>
<html lang="en">
<head>
<meta charset="utf-8">
<title>Pine Hollow Builders – Flyer and Business Card</title>
<link rel="stylesheet" href="https://fonts.googleapis.com/css2?family=Montserrat:wght@400;500;600;800&display=swap">
<style>
  :root{
    --cream:#fbe8d3;
    --cream-deep:#f3d9bd;
    --orange:#f0921e;
    --orange-dark:#d97c0e;
    --ink:#3b3b3b;
    --white:#ffffff;
    --stage:#e9e7e4;
  }
  *{box-sizing:border-box;margin:0;padding:0}
  html,body{width:1200px;height:892px;overflow:hidden}
  body{background:var(--stage);font-family:"Montserrat",Arial,sans-serif;color:var(--ink);position:relative}

  .flyer{position:absolute;left:40px;top:30px;width:640px;height:832px;background:var(--cream);overflow:hidden;box-shadow:0 6px 18px rgba(0,0,0,.12)}
  .blueprint{position:absolute;right:0;top:0;width:420px;height:300px;background:linear-gradient(160deg,#f6dfc5,var(--cream));opacity:.9}
  .headline{position:absolute;left:44px;top:52px;font-weight:800;font-size:40px;line-height:1.02;letter-spacing:.5px;text-transform:uppercase}
  .headline .accent{color:var(--orange)}
  .intro{position:absolute;left:44px;top:232px;width:285px;font-size:13px;line-height:1.45}
  .photos{position:absolute;left:44px;top:352px;width:250px}
  .photo{height:78px;margin-bottom:8px;border:4px solid var(--white);box-shadow:0 2px 6px rgba(0,0,0,.18);background:linear-gradient(135deg,#6d5a45,#c9a983 55%,#8a7054)}
  .photo:nth-child(2){margin-left:40px;background:linear-gradient(135deg,#b59c7c,#e9d8bf,#7f6a52)}
  .photo:nth-child(3){margin-left:14px;background:linear-gradient(135deg,#3f3a33,#b98f5a,#e2cfb2)}
  .contractor-photo{position:absolute;right:0;top:230px;width:290px;height:350px;background:linear-gradient(180deg,#e9d3b8 0%,#8a7a84 45%,#6e5a48 100%);opacity:.95}
  .about{position:absolute;left:44px;top:624px;width:285px;font-size:13px;line-height:1.45}
  .services{position:absolute;left:44px;top:690px;width:300px;font-size:11.5px;line-height:1.7;color:var(--orange);font-weight:600;white-space:nowrap}
  .services .sep{color:var(--ink);font-weight:400;padding:0 4px}
  .contact-band{position:absolute;right:0;top:596px;width:280px;height:126px;background:var(--orange);color:var(--white);padding:16px 18px;font-size:11.5px;line-height:1.35}
  .contact-band p{display:flex;align-items:center;gap:8px;margin-bottom:7px}
  .contact-band .phone{font-size:19px;font-weight:800}
  .contact-band svg{flex:none}
  .brand{position:absolute;left:360px;top:746px;width:260px}
  .brand-name{display:flex;align-items:center;gap:9px;font-weight:800;font-size:17px;color:var(--ink);white-space:nowrap}
  .brand-mark{width:26px;height:26px;background:var(--orange);flex:none}
  .license{font-size:10px;margin-top:6px;margin-left:35px;white-space:nowrap}

  .card{position:absolute;left:730px;width:420px;height:240px;box-shadow:0 6px 14px rgba(0,0,0,.12)}
  .card-front{top:140px;background:var(--cream);display:flex;align-items:center;justify-content:center}
  .card-front .brand-name{font-size:21px}
  .card-front .brand-mark{width:30px;height:30px}
  .card-back{top:470px;background:var(--orange);color:var(--white);padding:46px 40px;font-size:13px;line-height:1.7}
  .card-back .phone{font-weight:800}
  .card-back hr{border:0;border-top:1px solid rgba(255,255,255,.6);margin:10px 0}
</style>
</head>
<body>

<section class="flyer">
  <div class="blueprint" role="img" aria-label="Faint architectural blueprint line drawing of a house"></div>

  <h1 class="headline">Home<br><span class="accent">Renovation and<br>Construction</span><br>Service</h1>

  <p class="intro">We Specialize in Bathroom and Kitchen Remodeling, New Construction &amp; Interior or Exterior Home Renovations, Garages and more! Serving Central Florida for over 15 years.</p>

  <div class="photos">
    <div class="photo" role="img" aria-label="Photo of a remodeled kitchen"></div>
    <div class="photo" role="img" aria-label="Photo of a remodeled bathroom"></div>
    <div class="photo" role="img" aria-label="Photo of a modern kitchen interior"></div>
  </div>

  <div class="contractor-photo" role="img" aria-label="Photo of a contractor in a yellow hard hat holding rolled blueprints"></div>

  <p class="about">Family owned and operated.<br>We perform all levels of building and remodeling.</p>

  <p class="services">
    Bathrooms Kitchens<span class="sep">|</span>Tiling Painting<span class="sep">|</span>Decorating<br>
    Plastering<span class="sep">|</span>Carpentry<span class="sep">|</span>Flooring<span class="sep">|</span>Plumbing<br>
    Electrical Works<span class="sep">|</span>Brickwork<span class="sep">|</span>General Repairs
  </p>

  <div class="contact-band">
    <p><svg width="12" height="14" viewBox="0 0 12 14"><path d="M6 0a5 5 0 0 1 5 5c0 4-5 9-5 9S1 9 1 5a5 5 0 0 1 5-5zm0 3a2 2 0 1 0 0 4 2 2 0 0 0 0-4z" fill="#fff"/></svg>418 NE Juniper Ave, Lakeview, FL 34999, USA</p>
    <p class="phone"><svg width="14" height="14" viewBox="0 0 14 14"><path d="M3 1l2 3-1.5 1.5a8 8 0 0 0 5 5L10 9l3 2-1 2.5C6 14 0 8 .5 2z" fill="#fff"/></svg>555-014-2273</p>
    <p><svg width="13" height="13" viewBox="0 0 13 13"><circle cx="6.5" cy="6.5" r="5.5" fill="none" stroke="#fff" stroke-width="1.4"/><path d="M1 6.5h11M6.5 1c3 3 3 8 0 11M6.5 1c-3 3-3 8 0 11" fill="none" stroke="#fff" stroke-width="1"/></svg>www.brightmortarworks.example</p>
  </div>

  <div class="brand">
    <div class="brand-name"><span class="brand-mark"></span>PINE HOLLOW BUILDERS</div>
    <p class="license">FL State Lic. #CRC8047163 &amp; Insured</p>
  </div>
</section>

<section class="card card-front">
  <div class="brand-name"><span class="brand-mark"></span>PINE HOLLOW BUILDERS</div>
</section>

<section class="card card-back">
  <p>New Construction | Bath Remodels | Renovations</p>
  <p>Repairs | Kitchens | Bathrooms</p>
  <hr>
  <p>418 NE Juniper Ave, Lakeview, FL 34999, USA</p>
  <p><span class="phone">555-014-2273</span> &nbsp;|&nbsp; www.brightmortarworks.example</p>
</section>

</body>
</html>
```